Startup Biz for Seniors needs your help!

Our business is a Startup that Employs Caregivers to do IN HOME Care of the Elderly. Our website is not yet running. But, a business similar to ours is Tallbrookcare.com

We are looking for a card that only has 4 Elements:
-Logo
- Website
- Tag Line
- Phone
We would like to see some eye catching backgrounds.
We would like to see some designs with and some without a Photo.
Would like the Photo to be of a Caregiver taking care of a Senior. The photo should show both of them smiling.

Target Market(s)

Age 35-55 who has Parents that are Elderly and need care

Industry/Entity Type

Home Health Care

Contact Information for Business Card

Want it to Pop Out to the viewer . Thinking maybe:
Side 1: LOGO with Website & Tag line
Side 2: Phone Number

Font styles to use
Other font styles liked:
• Same Font as our Logo

Colors

Designer to choose colors to be used in the design.

Requirements
Must have
• Logo, website, Tag Line, Phone number and Email: "info@velvetdays.example"
• Please use one of the photos that I have attached.
Nice to have
• Would like to see a Photo worked in that has a Care Taker taking care of an Elderly Person and they are both smiling.

```html
<!DOCTYPE html>
<html lang="en">
<head>
<meta charset="utf-8">
<title>VelvetDays.example business card</title>
<link rel="stylesheet" href="https://fonts.googleapis.com/css2?family=Open+Sans:wght@400;600;700&display=swap">
<style>
  :root {
    --brand-blue: #0b56a6;
    --brand-orange: #ef5a24;
    --ink-grey: #5a5a5a;
    --paper: #ffffff;
    --paper-soft: rgba(255,255,255,.85);
    --backdrop: #2e2e30;
  }
  * { box-sizing: border-box; margin: 0; padding: 0; }
  html, body { width: 1200px; height: 900px; overflow: hidden; }
  body {
    background: var(--backdrop);
    font-family: "Open Sans", Arial, sans-serif;
    position: relative;
  }
  .card {
    position: absolute;
    left: 259px;
    width: 682px;
    height: 390px;
    box-shadow: 0 10px 30px rgba(0,0,0,.45);
  }
  .card--front { top: 40px; background: var(--brand-blue); }
  .card--back { top: 470px; background: var(--paper); }

  .brand {
    position: absolute;
    left: 0; right: 0;
    display: flex;
    justify-content: center;
    align-items: center;
    gap: 16px;
  }
  .brand__dot {
    width: 62px; height: 62px;
    border-radius: 50%;
    background: var(--brand-orange);
    flex: none;
  }
  .brand__name {
    font-weight: 700;
    font-size: 40px;
    line-height: 1;
    letter-spacing: .5px;
  }
  .card--front .brand { top: 148px; }
  .card--front .brand__name { color: var(--paper); }
  .card--back .brand { top: 64px; }
  .card--back .brand__name { color: var(--brand-blue); }

  .tagline {
    position: absolute;
    left: 0; right: 0;
    text-align: center;
    font-weight: 400;
    font-size: 20px;
    letter-spacing: 1px;
  }
  .card--front .tagline { top: 228px; color: var(--paper-soft); }
  .card--back .tagline { top: 144px; color: var(--ink-grey); }

  .contact-block {
    position: absolute;
    left: 0; right: 0; top: 250px;
    display: flex;
    justify-content: center;
    align-items: center;
  }
  .person { text-align: right; padding-right: 24px; }
  .person__name {
    color: var(--brand-blue);
    font-weight: 700;
    font-size: 30px;
    letter-spacing: 1.5px;
    text-transform: uppercase;
  }
  .person__title { color: var(--ink-grey); font-size: 22px; }
  .divider { width: 2px; height: 80px; background: var(--brand-blue); }
  .details { list-style: none; padding-left: 22px; }
  .details li {
    display: flex; align-items: center; gap: 8px;
    color: var(--ink-grey); font-size: 22px; line-height: 1.25;
  }
  .details svg { width: 16px; height: 16px; flex: none; fill: var(--brand-orange); }
</style>
</head>
<body>
  <section class="card card--front">
    <div class="brand">
      <span class="brand__dot"></span>
      <div class="brand__name">VelvetDays.example</div>
    </div>
    <p class="tagline">Caring Hands at Home</p>
  </section>

  <section class="card card--back">
    <div class="brand">
      <span class="brand__dot"></span>
      <div class="brand__name">VelvetDays.example</div>
    </div>
    <p class="tagline">Caring Hands at Home</p>

    <div class="contact-block">
      <div class="person">
        <div class="person__name">Dana Whitlow</div>
        <div class="person__title">President</div>
      </div>
      <div class="divider"></div>
      <ul class="details">
        <li>
          <svg viewBox="0 0 24 24" aria-hidden="true"><path d="M6.6 10.8a15 15 0 0 0 6.6 6.6l2.2-2.2a1 1 0 0 1 1-.25 11.4 11.4 0 0 0 3.6.57 1 1 0 0 1 1 1V20a1 1 0 0 1-1 1A17 17 0 0 1 3 4a1 1 0 0 1 1-1h3.5a1 1 0 0 1 1 1c0 1.25.2 2.45.57 3.57a1 1 0 0 1-.25 1z"/></svg>
          555.014.0272
        </li>
        <li>
          <svg viewBox="0 0 24 24" aria-hidden="true"><path d="M2 5h20v2l-10 6L2 7zm0 4 10 6 10-6v10H2z"/></svg>
          info@velvetdays.example
        </li>
        <li>
          <svg viewBox="0 0 24 24" aria-hidden="true"><circle cx="12" cy="12" r="10"/></svg>
          www.velvetdays.example
        </li>
      </ul>
    </div>
  </section>
</body>
</html>
```